A Weather Forecasting Site needs designs

We need a website design for our new venture which is a weather forecasting website. This website should have the latest design trends.

Menu
Weather, Maps, Videos and Photos

The home page requirements are as follows:
- Search Bar
- Local Weather
- Weather forecast of major cities in the World
Favorite locations
- Space for ADs
- Email signup

Weather Details page
This page will be redirected from the home page when you click on any of the weather forecast section

We are open to all kinds of designs and ideas. Feel free to you colors which suite your design.

```html
<!DOCTYPE html>
<html lang="en">
<head>
<meta charset="utf-8">
<title>Skyvale – Weather Forecasting</title>
<link href="https://fonts.googleapis.com/css2?family=Nunito:wght@300;400;600;700;800&display=swap" rel="stylesheet">
<style>
:root{
  --blue:#1c9ad6;
  --blue-dark:#1479b3;
  --pink:#d64f6f;
  --ink:#222;
  --muted:#666;
  --footer:#1a1e28;
  --white:#fff;
}
*{box-sizing:border-box;margin:0;padding:0}
html,body{width:1200px;height:2946px;overflow:hidden}
body{font-family:"Nunito",sans-serif;color:var(--ink);background:#fff;position:relative}
.wrap{width:1030px;margin:0 auto;position:relative}
/* header */
.site-header{height:90px;background:#fff;display:flex;align-items:center}
.site-header .wrap{display:flex;align-items:center;justify-content:space-between}
.brand{display:flex;align-items:center;gap:12px;font-weight:800;font-size:25px;color:#1e2a36;letter-spacing:.5px}
.brand-dot{width:40px;height:40px;border-radius:50%;background:var(--blue)}
.main-nav{display:flex;align-items:center;gap:32px;font-size:16px;color:#222}
.main-nav .active{color:var(--blue)}
.call-btn{width:36px;height:36px;border:2px solid var(--blue);border-radius:50%;display:flex;align-items:center;justify-content:center;margin-left:4px}
/* hero */
.hero{height:488px;position:relative;background:linear-gradient(120deg,#2b3a4a 0%,#3f4c57 40%,#5a6670 60%,#2d3a34 100%);color:#fff;text-align:center}
.hero h1{font-weight:400;font-size:38px;padding-top:166px;letter-spacing:.5px}
.hero p{font-size:19px;margin-top:4px}
.search{display:flex;width:634px;margin:22px auto 0;height:58px}
.search input{flex:1;border:0;padding:0 22px;font:15px "Nunito",sans-serif;color:#555}
.search button{width:108px;border:0;background:var(--pink);color:#fff;font:14px "Nunito",sans-serif;display:flex;align-items:center;justify-content:center;gap:6px}
.hero-arrow{position:absolute;top:248px;width:24px;height:24px;border-radius:50%;background:rgba(0,0,0,.6);display:flex;align-items:center;justify-content:center}
/* local weather */
.local{height:102px;background:linear-gradient(90deg,var(--blue-dark),var(--blue) 60%,var(--blue-dark));color:#fff}
.local .wrap{height:102px;display:flex;align-items:center;justify-content:space-between}
.local h2{font-weight:400;font-size:26px}
.local p{font-size:15px;margin-top:2px}
.local-now{width:298px;height:102px;background:rgba(255,255,255,.18);display:flex;align-items:center;gap:18px;padding-left:28px}
.local-now .place{font-size:20px;line-height:1}
.local-now small{font-size:11px}
.local-now .temp{font-size:54px;font-weight:300}
/* welcome */
.welcome{height:430px}
.welcome .wrap{display:flex;justify-content:space-between;align-items:center;height:430px;padding-left:20px}
.welcome h2{font-weight:400;font-size:30px;margin-bottom:16px}
.welcome p{width:550px;font-size:13px;line-height:22px;color:var(--muted)}
.pill{display:inline-block;background:var(--pink);color:#fff;border-radius:16px;font-size:11px;padding:7px 18px;margin-top:22px}
.globe{width:310px;height:310px;border-radius:50%;background:radial-gradient(circle at 40% 35%,#bfe6f8,#3a9bd8 55%,#1b5f9e);margin-right:46px}
/* cities */
.cities{height:520px;position:relative;background:linear-gradient(180deg,#141a22,#2a3038 50%,#151a20);color:#fff}
.cities h2{text-align:center;font-weight:400;font-size:29px;padding-top:74px}
.city-row{display:flex;gap:8px;margin-top:38px}
.city{width:338px;height:287px;position:relative;padding:20px 38px 0 32px}
.city.ny{background:linear-gradient(180deg,#8e8b86,#5c4e44 60%,#2a2623)}
.city.dubai{background:linear-gradient(180deg,#9fb4c8,#687f93 60%,#2b3540)}
.city.toronto{background:linear-gradient(180deg,#5c93d1,#6c8fae 60%,#28323d)}
.city .day{font-size:22px;line-height:1;padding-left:8px}
.city .date{font-size:10px;padding-left:8px}
.city .temp{font-size:80px;font-weight:800;line-height:1;margin-top:0}
.city .temp sup{font-size:44px;vertical-align:top;line-height:1}
.city .name{font-size:13px}
.city .wind{display:flex;align-items:center;gap:8px;font-size:17px;font-weight:700;margin-top:4px}
.forecast{position:absolute;left:0;right:0;bottom:0;height:82px;display:flex;align-items:center;padding:0 10px}
.forecast .nav{width:20px;text-align:center;font-size:22px}
.forecast ul{flex:1;display:flex;list-style:none}
.forecast li{flex:1;text-align:center;font-size:11px;border-right:1px solid rgba(255,255,255,.35);line-height:1.3}
.forecast li svg{display:block;margin:2px auto}
.forecast li:last-child{border-right:0}
.cities .side{position:absolute;top:368px}
/* about */
.about{height:490px;padding-top:75px}
.about-card{width:900px;height:328px;margin:0 auto;display:flex;box-shadow:0 2px 10px rgba(0,0,0,.18)}
.about-media{width:392px;height:328px;background:linear-gradient(135deg,#4c6b8a,#8a99a6 50%,#2f3d4b);display:flex;align-items:center;justify-content:center}
.about-text{padding:58px 36px 0 46px;flex:1}
.about-text h2{font-weight:400;font-size:30px}
.about-text h3{font-weight:400;font-size:16px;color:#444;margin-top:2px}
.about-text p{font-size:13px;line-height:22px;color:var(--muted);margin-top:14px}
.about-text .pill{font-size:13px;padding:8px 18px;margin-top:20px}
/* map */
.map{height:325px;position:relative;background:linear-gradient(135deg,#e6e6e6,#d9d9d9 50%,#e8e8e8)}
.map-card{position:absolute;left:244px;top:92px;width:240px;height:106px;background:#fff;box-shadow:0 2px 8px rgba(0,0,0,.2);display:flex;align-items:center;gap:16px;padding-left:24px}
.map-card .place{font-size:21px;line-height:1}
.map-card small{font-size:11px}
.map-card .temp{font-size:50px;font-weight:300;color:var(--blue)}
.map-pin{position:absolute;left:560px;top:148px}
/* ad */
.ad{height:225px;padding-top:48px}
.ad-slot{width:1008px;height:142px;margin:0 auto;background:#3d3f42;padding:8px}
.ad-slot div{width:100%;height:100%;background:linear-gradient(90deg,#1c3f7a,#2c62a8 50%,#1a5a8f)}
/* footer */
.site-footer{height:275px;background:var(--footer);color:#fff;position:relative}
.footer-cols{display:flex;padding-top:62px}
.footer-cols h4{font-weight:400;font-size:15px;letter-spacing:.5px;margin-bottom:20px;white-space:nowrap}
.col-nav{width:252px}
.col-contact{width:308px}
.col-news{width:293px}
.col-follow{width:180px}
.col-nav ul{list-style:none;font-size:11px;line-height:22px}
.col-nav li::before{content:"» "}
.col-contact p{font-size:11px;line-height:22px}
.col-news p{font-size:11px;line-height:16px;width:190px}
.signup{display:flex;margin-top:14px;height:30px}
.signup input{width:148px;border:0;padding:0 8px;font:11px "Nunito",sans-serif}
.signup button{width:54px;border:0;background:var(--pink);color:#fff;font:11px "Nunito",sans-serif}
.social{display:flex;gap:14px}
.social span{width:25px;height:25px;background:#fff;border-radius:3px}
.copyright{position:absolute;bottom:20px;width:100%;text-align:center;font-size:12px}
</style>
</head>
<body>
<header class="site-header">
  <div class="wrap">
    <div class="brand"><span class="brand-dot"></span>SKYVALE</div>
    <nav class="main-nav">
      <span class="active">HOME</span><span>WEATHER</span><span>MAPS</span><span>VIDEOS</span><span>PHOTOS</span><span>ABOUT</span><span>CONTACT</span>
      <span class="call-btn"><svg width="16" height="16" viewBox="0 0 24 24"><path fill="#1c9ad6" d="M6.6 10.8a15 15 0 0 0 6.6 6.6l2.2-2.2c.3-.3.7-.4 1-.2 1.1.4 2.3.6 3.6.6.6 0 1 .4 1 1V20c0 .6-.4 1-1 1A17 17 0 0 1 3 4c0-.6.4-1 1-1h3.5c.6 0 1 .4 1 1 0 1.3.2 2.5.6 3.6.1.3 0 .7-.2 1z"/></svg></span>
    </nav>
  </div>
</header>

<section class="hero" role="img" aria-label="Weather presenter standing before a satellite view of cloud systems">
  <h1>WEATHER FORECASTING</h1>
  <p>Neque porro quisquam est qui dolorem ipsum</p>
  <form class="search">
    <input type="text" placeholder="Search">
    <button type="button"><svg width="12" height="12" viewBox="0 0 24 24"><circle cx="10" cy="10" r="7" stroke="#fff" stroke-width="3" fill="none"/><path d="M15 15l6 6" stroke="#fff" stroke-width="3"/></svg>SEARCH</button>
  </form>
  <span class="hero-arrow" style="left:70px"><svg width="10" height="10" viewBox="0 0 10 10"><path d="M6.5 1.5L3 5l3.5 3.5" stroke="#fff" stroke-width="1.6" fill="none"/></svg></span>
  <span class="hero-arrow" style="left:1106px"><svg width="10" height="10" viewBox="0 0 10 10"><path d="M3.5 1.5L7 5 3.5 8.5" stroke="#fff" stroke-width="1.6" fill="none"/></svg></span>
</section>

<section class="local">
  <div class="wrap">
    <div>
      <h2>Local Weather</h2>
      <p>Neque porro quisquam est qui dolorem ipsum quia dolor sit amet, consectetur, adipisci velit...</p>
    </div>
    <div class="local-now">
      <div><div class="place">canada</div><small>2:00 pm</small></div>
      <div class="temp">14°</div>
      <svg width="60" height="48" viewBox="0 0 60 48"><circle cx="24" cy="18" r="12" fill="#f6c342"/><path d="M18 40h30a9 9 0 0 0-2-17.8A12 12 0 0 0 23 26a7 7 0 0 0-5 14z" fill="#fff"/><path d="M26 44l-2 3M34 44l-2 3M42 44l-2 3" stroke="#fff" stroke-width="2"/></svg>
    </div>
  </div>
</section>

<section class="welcome">
  <div class="wrap">
    <div>
      <h2>WELCOME TO SKYVALE</h2>
      <p>It is a long established fact that a reader will be distracted by the readable content of a page when looking at its layout. The point of using Lorem Ipsum is that it has a more-or-less normal distribution of letters, as opposed to using 'Content here, content here', making it look like readable English. Many desktop publishing packages and web page editors now use Lorem Ipsum as their default model text, and a search for 'lorem ipsum' will uncover many web sites still in their infancy. Various versions have evolved over the years, sometimes by accident, sometimes on purpose</p>
      <span class="pill">Read More »</span>
    </div>
    <div class="globe" role="img" aria-label="Illustration of a glossy globe with sun, clouds and rain"></div>
  </div>
</section>

<section class="cities" role="img" aria-label="Dark night city skyline backdrop">
  <h2>WEATHER FORECAST OF MAJOR CITIES IN THE WORLD</h2>
  <svg class="side" style="left:42px" width="20" height="36" viewBox="0 0 20 36"><path d="M18 2L3 18l15 16" stroke="#fff" stroke-width="1.5" fill="none"/></svg>
  <svg class="side" style="left:1136px" width="20" height="36" viewBox="0 0 20 36"><path d="M2 2l15 16L2 34" stroke="#fff" stroke-width="1.5" fill="none"/></svg>
  <div class="wrap city-row">
    <article class="city ny" aria-label="New York skyline photo">
      <div class="day">Sunday</div><div class="date">June, 26th</div>
      <div class="temp">15<sup>°</sup></div><div class="name">New York, usa</div>
      <div class="wind"><svg width="34" height="14" viewBox="0 0 34 14"><path d="M0 4h22a3 3 0 1 0-3-3M0 9h30a3 3 0 1 1-3 3" stroke="#fff" stroke-width="2" fill="none"/></svg>12 mph</div>
      <div class="forecast"><span class="nav">‹</span><ul>
        <li>Monday<svg width="28" height="22" viewBox="0 0 28 22"><path d="M7 14h15a5 5 0 0 0-1-9.9A7 7 0 0 0 8 7a3.6 3.6 0 0 0-1 7z" stroke="#fff" stroke-width="1.4" fill="none"/><path d="M10 17l-1 3M15 17l-1 3M20 17l-1 3" stroke="#fff" stroke-width="1.4"/></svg>10</li>
        <li>Tuesday<svg width="28" height="22" viewBox="0 0 28 22"><path d="M6 17h16a5 5 0 0 0-1-9.9A7 7 0 0 0 7 10a3.6 3.6 0 0 0-1 7z" stroke="#fff" stroke-width="1.4" fill="none"/></svg>15</li>
        <li>Wednesday<svg width="28" height="22" viewBox="0 0 28 22"><circle cx="14" cy="11" r="5" stroke="#fff" stroke-width="1.4" fill="none"/><path d="M14 1v3M14 18v3M4 11h3M21 11h3M7 4l2 2M19 16l2 2M21 4l-2 2M9 16l-2 2" stroke="#fff" stroke-width="1.4"/></svg>23</li>
      </ul><span class="nav">›</span></div>
    </article>
    <article class="city dubai" aria-label="Dubai skyline photo">
      <div class="day">Sunday</div><div class="date">June, 26th</div>
      <div class="temp">14<sup>°</sup></div><div class="name">Dubai</div>
      <div class="wind"><svg width="34" height="14" viewBox="0 0 34 14"><path d="M0 4h22a3 3 0 1 0-3-3M0 9h30a3 3 0 1 1-3 3" stroke="#fff" stroke-width="2" fill="none"/></svg>11 mph</div>
      <div class="forecast"><span class="nav">‹</span><ul>
        <li>Monday<svg width="28" height="22" viewBox="0 0 28 22"><path d="M7 14h15a5 5 0 0 0-1-9.9A7 7 0 0 0 8 7a3.6 3.6 0 0 0-1 7z" stroke="#fff" stroke-width="1.4" fill="none"/><path d="M10 17l-1 3M15 17l-1 3M20 17l-1 3" stroke="#fff" stroke-width="1.4"/></svg>10</li>
        <li>Tuesday<svg width="28" height="22" viewBox="0 0 28 22"><path d="M6 17h16a5 5 0 0 0-1-9.9A7 7 0 0 0 7 10a3.6 3.6 0 0 0-1 7z" stroke="#fff" stroke-width="1.4" fill="none"/></svg>15</li>
        <li>Wednesday<svg width="28" height="22" viewBox="0 0 28 22"><circle cx="14" cy="11" r="5" stroke="#fff" stroke-width="1.4" fill="none"/><path d="M14 1v3M14 18v3M4 11h3M21 11h3M7 4l2 2M19 16l2 2M21 4l-2 2M9 16l-2 2" stroke="#fff" stroke-width="1.4"/></svg>23</li>
      </ul><span class="nav">›</span></div>
    </article>
    <article class="city toronto" aria-label="Toronto skyline photo">
      <div class="day">Sunday</div><div class="date">June, 26th</div>
      <div class="temp">12<sup>°</sup></div><div class="name">Canada, Toronto</div>
      <div class="wind"><svg width="34" height="14" viewBox="0 0 34 14"><path d="M0 4h22a3 3 0 1 0-3-3M0 9h30a3 3 0 1 1-3 3" stroke="#fff" stroke-width="2" fill="none"/></svg>10 mph</div>
      <div class="forecast"><span class="nav">‹</span><ul>
        <li>Monday<svg width="28" height="22" viewBox="0 0 28 22"><path d="M7 14h15a5 5 0 0 0-1-9.9A7 7 0 0 0 8 7a3.6 3.6 0 0 0-1 7z" stroke="#fff" stroke-width="1.4" fill="none"/><path d="M10 17l-1 3M15 17l-1 3M20 17l-1 3" stroke="#fff" stroke-width="1.4"/></svg>10</li>
        <li>Tuesday<svg width="28" height="22" viewBox="0 0 28 22"><path d="M6 17h16a5 5 0 0 0-1-9.9A7 7 0 0 0 7 10a3.6 3.6 0 0 0-1 7z" stroke="#fff" stroke-width="1.4" fill="none"/></svg>15</li>
        <li>Wednesday<svg width="28" height="22" viewBox="0 0 28 22"><circle cx="14" cy="11" r="5" stroke="#fff" stroke-width="1.4" fill="none"/><path d="M14 1v3M14 18v3M4 11h3M21 11h3M7 4l2 2M19 16l2 2M21 4l-2 2M9 16l-2 2" stroke="#fff" stroke-width="1.4"/></svg>23</li>
      </ul><span class="nav">›</span></div>
    </article>
  </div>
</section>

<section class="about">
  <div class="about-card">
    <div class="about-media" role="img" aria-label="Video still of a presenter holding a folder before a satellite weather map">
      <svg width="54" height="54" viewBox="0 0 54 54"><circle cx="27" cy="27" r="26" fill="rgba(0,0,0,.55)"/><path d="M21 16l17 11-17 11z" fill="#fff"/></svg>
    </div>
    <div class="about-text">
      <h2>WHAT WE DO</h2>
      <h3>Neque porro quisquam dolorem ipsum</h3>
      <p>It is a long established fact that a reader will be distracted by the readable content of a page when looking at its layout. The point of using Lorem Ipsum is that it has a more-or-less normal distribution of letters, as opposed to using 'Content here, content here',</p>
      <span class="pill">READ MORE</span>
    </div>
  </div>
</section>

<section class="map" role="img" aria-label="Street map of the local area">
  <div class="map-card">
    <div><div class="place">Location</div><small>2:00 pm</small></div>
    <div class="temp">12°</div>
    <svg width="50" height="40" viewBox="0 0 50 40"><circle cx="18" cy="15" r="10" fill="#f6c342"/><path d="M14 34h26a8 8 0 0 0-2-15.7A10 10 0 0 0 19 21a6.5 6.5 0 0 0-5 13z" fill="#cfd6dc"/></svg>
  </div>
  <svg class="map-pin" width="46" height="64" viewBox="0 0 46 64"><path d="M23 0a23 23 0 0 1 23 23c0 17-23 41-23 41S0 40 0 23A23 23 0 0 1 23 0z" fill="#e0534f"/><circle cx="23" cy="22" r="8" fill="#b83a37"/></svg>
</section>

<section class="ad">
  <div class="ad-slot"><div role="img" aria-label="Advertisement banner"></div></div>
</section>

<footer class="site-footer">
  <div class="wrap footer-cols">
    <div class="col-nav">
      <h4>NAVIGATION</h4>
      <ul><li>Aboutus</li><li>services</li><li>Testimonials</li><li>Weather</li></ul>
    </div>
    <div class="col-contact">
      <h4>CONTACT US</h4>
      <p>Address : 12 Fernway rd, Elm Quarter<br>Avonby, Av4 2KL<br>Phone : 01234 567890<br>Email : hello@skymail.test</p>
    </div>
    <div class="col-news">
      <h4>SIGN UP FOR NEWSLETTER</h4>
      <p>Your about us information would fit here nicely.</p>
      <form class="signup"><input type="email" placeholder="Email address"><button type="button">Submit</button></form>
    </div>
    <div class="col-follow">
      <h4>FOLLOW US OUT THERE</h4>
      <div class="social"><span></span><span></span><span></span><span></span></div>
    </div>
  </div>
  <p class="copyright">Copyright © 2017. All Rights Reserved</p>
</footer>
</body>
</html>
```